Book cover - Quiet Rooms, Open Doors

Book cover for Ebook (Pagelight) and wrap around print cover (Printvale) (back, front, and spine)

The book title (may slightly change by end of brief):
(MAIN TITLE) 'Quiet Rooms, Open Doors'
(SUB HEADING) 'A Week-by-Week Practical Workbook to Loosen Nervous Habits, Quieten Doubt and Build Steady Poise'
by Dr Owen Hartley

I would like a bold, stand out cover. Contemporary. I would like to avoid stereotypical images of people looking anxious or worried. I would like the design to be more uplifting and hopeful, rather than focusing on the negative aspect of anxiety, but avoiding cliched photos of people raising their hands in the air, smiling and jumping etc. The cover should appeal to both men and women.

Trim size of book cover (for PrintVale) is 5.25" x 8" back and front with a spine size of 0.477 inches

Reason: I have decided to extend the deadline by 1 more day, not because I am unhappy with the quality of the designs, but because a few designers have contacted me to explain they have had technical difficulties when submitting their files. Thanks everyone for the hard work and great designs.

Target Market(s)

Males and females (16+) who struggle with social anxiety and shyness

Industry/Entity Type

Social

Font styles to use
Serif

Requirements
Must have
• Bold cover that is modern and contemporary. For example, I like these covers:
• http://shrtlnk.example/k4Tq9Zb
• http://shrtlnk.example/m8Wv2Hn
• http://shrtlnk.example/p3Jx6Lr
• http://shrtlnk.example/t7Gd1Qe
• http://shrtlnk.example/v2Nk8Fy
• http://shrtlnk.example/w9Bh4Cs
• http://shrtlnk.example/z5Mf3Ud
Nice to have
• Open to abstract designs.
Should not have
• No stereotypical pictures of people who look anxious or worried. Avoid cliched photos of people raising their hands in the air, smiling and jumping etc.

```html
<!DOCTYPE html>
<html lang="en">
<head>
<meta charset="utf-8">
<title>Quiet Rooms, Open Doors – Wraparound Book Cover</title>
<link rel="stylesheet" href="https://fonts.googleapis.com/css2?family=Alfa+Slab+One&family=Roboto+Slab:wght@700;900&display=swap">
<style>
  :root {
    --backdrop: #e9eaec;
    --cover-cyan: #3ccbef;
    --cover-cyan-deep: #2cb9e3;
    --spine-cyan: #2fb3dc;
    --title-white: #ffffff;
    --ink-teal: #1f4d5e;
    --ink-dark: #173443;
    --cloud: #f2fbfe;
  }
  html, body {
    margin: 0;
    padding: 0;
    width: 1200px;
    height: 1172px;
    overflow: hidden;
    background: var(--backdrop);
  }
  .canvas {
    position: relative;
    width: 1200px;
    height: 1172px;
  }
  .wraparound {
    position: absolute;
    left: 51px;
    top: 186px;
    width: 1098px;
    height: 800px;
    display: flex;
  }
  .back-cover,
  .front-cover {
    position: relative;
    width: 525px;
    height: 100%;
    background: linear-gradient(180deg, var(--cover-cyan) 0%, var(--cover-cyan-deep) 100%);
    overflow: hidden;
  }
  .spine {
    position: relative;
    width: 48px;
    height: 100%;
    background: var(--spine-cyan);
    overflow: hidden;
  }
  .spine-text {
    position: absolute;
    left: 50%;
    top: 50%;
    transform: translate(-50%, -50%) rotate(-90deg);
    white-space: nowrap;
    font-family: "Roboto Slab", serif;
    font-weight: 700;
    font-size: 21px;
    color: var(--title-white);
  }
  .cloud {
    position: absolute;
    background: var(--cloud);
    border-radius: 50%;
  }
  .back-cover .cloud { left: 150px; top: 200px; width: 70px; height: 40px; }
  .front-cover .cloud.top { left: 170px; top: -22px; width: 90px; height: 48px; }
  .front-cover .cloud.side { right: -30px; top: 118px; width: 84px; height: 54px; }
  .author {
    position: absolute;
    top: 34px;
    left: 0;
    right: 0;
    text-align: center;
    font-family: "Roboto Slab", serif;
    font-weight: 900;
    font-size: 30px;
    color: var(--title-white);
  }
  .title-line-one {
    position: absolute;
    top: 74px;
    left: 0;
    right: 0;
    text-align: center;
    font-family: "Alfa Slab One", serif;
    font-size: 68px;
    line-height: 1;
    color: var(--title-white);
  }
  .title-line-two {
    position: absolute;
    top: 150px;
    left: 0;
    right: 0;
    text-align: center;
    font-family: "Alfa Slab One", serif;
    font-size: 96px;
    line-height: 1;
    color: var(--title-white);
  }
  .figures-area {
    position: absolute;
    left: 110px;
    top: 275px;
    width: 320px;
    height: 230px;
  }
  .title-line-three {
    position: absolute;
    top: 520px;
    left: 0;
    right: 24px;
    text-align: right;
    font-family: "Roboto Slab", serif;
    font-weight: 900;
    font-size: 70px;
    line-height: 1;
    color: var(--ink-teal);
    letter-spacing: -1px;
  }
  .subtitle {
    position: absolute;
    left: 36px;
    right: 28px;
    top: 640px;
    text-align: center;
    font-family: "Roboto Slab", serif;
    font-weight: 700;
    font-size: 19px;
    line-height: 1.25;
    color: var(--ink-dark);
  }
</style>
</head>
<body>
<div class="canvas">
  <div class="wraparound">
    <div class="back-cover">
      <div class="cloud" role="img" aria-label="soft white cloud"></div>
    </div>
    <div class="spine">
      <div class="spine-text">Dr Owen Hartley &nbsp;Quiet Rooms, Open Doors</div>
    </div>
    <div class="front-cover">
      <div class="cloud top" role="img" aria-label="soft white cloud"></div>
      <div class="cloud side" role="img" aria-label="soft white cloud"></div>
      <div class="author">Dr Owen Hartley</div>
      <div class="title-line-one">Quiet</div>
      <div class="title-line-two">Rooms,</div>
      <svg class="figures-area" viewBox="0 0 320 230" role="img" aria-label="two white silhouetted figures leaping in the air">
        <defs>
          <radialGradient id="figureGlow" cx="50%" cy="50%" r="50%">
            <stop offset="0%" stop-color="#ffffff" stop-opacity="0.8"/>
            <stop offset="100%" stop-color="#ffffff" stop-opacity="0"/>
          </radialGradient>
        </defs>
        <ellipse cx="160" cy="115" rx="160" ry="115" fill="url(#figureGlow)"/>
      </svg>
      <div class="title-line-three">Open Doors</div>
      <div class="subtitle">‘A Week-by-Week Practical Workbook to Loosen Nervous Habits, Quieten Doubt and Build Steady Poise’</div>
    </div>
  </div>
</div>
</body>
</html>
```